Kept Until Book Cover

I am looking for book front cover ideas. The book trim size will be 5.5 x 8.5 in so please make the mock up that size. The book Title is "Kept Until" and the Subtitle is "Insight for the Hard Calls Every Chief Faces". The audience for the book is leaders in high-growth companies. It consists of a series of letters and advice for specific problems the leader will encounter on their journey. The design needs to be attractive to both male and female readers. I am attaching a file with brand colors and some rough ideas that need to be refined. The examples lean toward a feminine vibe but I want the cover to be more universal. Please use the brand colors identified in the file.

```html
<!DOCTYPE html>
<html lang="en">
<head>
<meta charset="utf-8">
<title>Kept Until – Book Cover</title>
<link rel="stylesheet" href="https://fonts.googleapis.com/css2?family=Fira+Sans:wght@600&family=Caveat:wght@700&family=Roboto:wght@700&display=swap">
<style>
  :root {
    --page-bg: #ffffff;
    --cover-paper: #f6f3ee;
    --title-clay: #b67d63;
    --subtitle-green: #2f5545;
    --band-blue: #869cb2;
    --author-white: #ffffff;
    --leaf-green: #5f8a72;
    --envelope-tan: #e2b894;
    --bloom-coral: #e0886a;
  }
  * { margin: 0; padding: 0; box-sizing: border-box; }
  html, body {
    width: 978px; height: 1200px; overflow: hidden;
    background: var(--page-bg);
  }
  .cover {
    position: absolute;
    left: 119px; top: 28px;
    width: 740px; height: 1144px;
    background: var(--cover-paper);
    overflow: hidden;
    box-shadow: 0 6px 24px rgba(0,0,0,0.12);
  }
  .title {
    position: absolute;
    left: 0; right: 0; top: 70px;
    text-align: center;
    font-family: "Fira Sans", sans-serif;
    font-weight: 600;
    font-size: 168px;
    line-height: 0.92;
    color: var(--title-clay);
    letter-spacing: -2px;
    text-shadow: 0 0 10px rgba(255,255,255,0.9);
    z-index: 2;
  }
  .title span { display: block; }
  .artwork {
    position: absolute;
    left: 150px; top: 300px;
    width: 440px; height: 460px;
    border-radius: 44% 44% 8px 8px;
    background:
      radial-gradient(ellipse at 50% 30%, rgba(224,136,106,0.55) 0%, rgba(224,136,106,0) 40%),
      radial-gradient(ellipse at 50% 35%, var(--leaf-green) 0%, rgba(95,138,114,0.6) 45%, rgba(95,138,114,0) 70%),
      linear-gradient(to bottom, rgba(226,184,148,0) 50%, var(--envelope-tan) 62%, var(--envelope-tan) 100%);
    z-index: 1;
  }
  .subtitle {
    position: absolute;
    left: 0; right: 0; top: 770px;
    text-align: center;
    font-family: "Caveat", cursive;
    font-weight: 700;
    font-size: 56px;
    line-height: 1.05;
    color: var(--subtitle-green);
  }
  .subtitle span { display: block; }
  .sprig {
    position: absolute;
    left: 320px; top: 930px;
    width: 100px; height: 26px;
    background: linear-gradient(to right, var(--leaf-green), rgba(95,138,114,0.55));
    border-radius: 13px;
  }
  .author-band {
    position: absolute;
    left: 0; bottom: 0;
    width: 740px; height: 190px;
  }
  .author-band svg { position: absolute; inset: 0; }
  .author {
    position: absolute;
    left: 0; right: 0; bottom: 62px;
    text-align: center;
    font-family: "Roboto", sans-serif;
    font-weight: 700;
    font-size: 32px;
    color: var(--author-white);
    letter-spacing: 0.3px;
  }
</style>
</head>
<body>
  <main class="cover">
    <h1 class="title"><span>Kept</span><span>Until</span></h1>

    <div class="artwork" role="img" aria-label="Watercolour illustration of an open kraft envelope overflowing with eucalyptus leaves and small coral and white flowers"></div>

    <p class="subtitle"><span>Insight for the Hard Calls</span><span>Every Chief Faces</span></p>

    <div class="sprig" role="img" aria-label="Small green leafy sprig ornament"></div>

    <footer class="author-band">
      <svg width="740" height="190" viewBox="0 0 740 190" aria-hidden="true">
        <polygon fill="var(--band-blue)" points="0,4 40,8 80,2 120,10 170,12 210,18 260,22 300,30 340,28 380,36 420,40 460,44 500,50 540,48 580,56 620,60 660,58 700,64 740,66 740,190 0,190"/>
      </svg>
      <p class="author">Mara Osei Linden</p>
    </footer>
  </main>
</body>
</html>
```